Flyer für Installationsfirma für hochwertige Multimedia- und Beschallungslösungen, insbesonder in Kirchen und öffentlichen Bereichen mit Menschenansammlungen
Zielgruppe
Wir sind eine Installationsfirma für hochwertige Multimedia- und Beschallungslösungen in akustisch schwierigen Räumen. Im weiteren auch der Umbau auf LED Leuchten und dazugehörende Steuerungen. Unser Geschäft ist in Festinstallationen und Rentalbereich 'unterteilt' Weitere Infos auch auf www. alpen-ton.ch
Unser Zielpublikum sind die Festinstallation für Kirchen und öffentliche Räume. Mehrzweckräume, Bühnen, Kirchen, Aulas, Bahnhofshallen, Warteräume, Konferenzräume, Tagungszentren usw. Bei diesem Flyer sollen speziell die Kirchen beworben werden. Es ist wichtig dass nebst den oben beschriebenen Leistungen auch die Displaylösung für Liedanzeigen hervorgehoben wird.
Aufgabenstellung
Ansprechender Werbe-Flyer A4 2 Seitig
Spezifische Bilder und Texte zu den versch. Angebotsbereichen für Kirchen im Anhang. Vorschläge des Grafikers sind willkommen !
Die Texte und Bilder sollten von uns angepasst und korrigiert werden können !

```html
<!DOCTYPE html>
<html lang="de">
<head>
<meta charset="utf-8">
<title>Alpenton – Flyer Kirchen</title>
<link href="https://fonts.googleapis.com/css2?family=Open+Sans:wght@400;600;700&family=Poppins:wght@500;600;700&family=Roboto:wght@500&display=swap" rel="stylesheet">
<style>
  :root{
    --bg:#e9e8e8;
    --navy:#172131;
    --navy-deep:#131b28;
    --footer:#1d3957;
    --accent:#2aa6e0;
    --white:#ffffff;
    --text:#d9dee6;
    --photo-warm:#d9c2a8;
    --photo-wood:#6b4a35;
  }
  *{margin:0;padding:0;box-sizing:border-box}
  html,body{width:1200px;height:800px;overflow:hidden;background:var(--bg)}
  .canvas{position:relative;width:1200px;height:800px}
  .page{position:absolute;top:18px;width:540px;height:764px;background:var(--navy);overflow:hidden;color:var(--white)}
  .page--front{left:40px}
  .page--back{left:620px;background:var(--navy-deep)}

  .hero-photo{position:absolute;left:0;top:0;width:540px;height:360px;
    background:linear-gradient(180deg,#cfc3b5 0%,var(--photo-warm) 30%,#a98a6c 50%,var(--photo-wood) 68%,#2b3140 88%,var(--navy) 100%)}
  .headline{position:absolute;left:0;top:334px;width:540px;text-align:center;font-family:'Poppins',sans-serif;font-weight:700;font-size:33px;line-height:41px;letter-spacing:-.3px}
  .accent{color:var(--accent)}
  .intro{position:absolute;left:38px;top:432px;width:464px;text-align:center;font-family:'Open Sans',sans-serif;font-size:9.6px;line-height:15.6px;color:var(--text)}
  .features{position:absolute;left:36px;top:552px;width:468px;display:flex;justify-content:space-between}
  .feature{width:117px;text-align:center;font-family:'Roboto',sans-serif;font-weight:500;font-size:15.5px;line-height:20px;color:var(--white)}
  .feature svg{display:block;margin:0 auto 14px;width:64px;height:64px}

  .footer{position:absolute;left:0;bottom:0;width:540px;height:70px;background:var(--footer);display:flex;align-items:center;padding-left:43px}
  .footer__name{font-family:'Poppins',sans-serif;font-weight:500;font-size:27px;letter-spacing:1.5px;color:var(--white);width:216px}
  .footer__contact{font-family:'Open Sans',sans-serif;font-weight:700;font-size:10.6px;line-height:18px;color:var(--white)}

  .services-title{position:absolute;left:0;top:36px;width:540px;text-align:center;font-family:'Poppins',sans-serif;font-weight:700;font-size:33px;letter-spacing:-.3px;text-shadow:0 0 22px rgba(42,166,224,.45)}
  .service{position:absolute;font-family:'Open Sans',sans-serif;font-size:9.4px;line-height:15.4px;color:var(--text)}
  .service h2{font-family:'Poppins',sans-serif;font-weight:600;font-size:15.5px;line-height:20px;color:var(--white);margin-bottom:6px}
  .service-photo{position:absolute;width:142px;height:96px;border:3px solid #f2f2f2}
  .cta{position:absolute;left:75px;top:611px;width:390px;height:61px;border:2px solid var(--accent);display:flex;align-items:center;justify-content:center;text-align:center;font-family:'Open Sans',sans-serif;font-weight:600;font-size:13px;line-height:19px;color:var(--white)}
</style>
</head>
<body>
<div class="canvas">

  <section class="page page--front">
    <div class="hero-photo" role="img" aria-label="Foto: Innenraum einer barocken Kirche mit Bankreihen, Altar und Kronleuchtern"></div>
    <h1 class="headline">BENÖTIGEN SIE <span class="accent">AUDIO &amp;</span><br><span class="accent">VISUAL</span> FÜR IHRE KIRCHE?</h1>
    <p class="intro">Multimediainstallation in Kirchen und Eventräumen Für heutige Gottesdienste und multifunktionellen Betrieb von Gotteshäusern wird eine moderne Medientechnik benötigt. Beschallungssysteme mit sehr guter Sprachverständlichkeit durch Beam-Steering Technologie und dezenter Optik, LED-Beleuchtung und Projektion sind selbstverständlich geworden. Gleichzeitig gehört eine Integration der Heizung und Glockensteuerung zusammen mit der AV-Installation und einfache Bedienung via Tablet zum heutigen Anforderungsprofil einer Kirche.</p>
    <div class="features">
      <div class="feature">
        <svg viewBox="0 0 64 64" fill="none" stroke="#fff" stroke-width="2"><circle cx="32" cy="26" r="20"/><circle cx="32" cy="26" r="14"/><path d="M22 43l-4 16 8-5 6 6M42 43l4 16-8-5-6 6"/><text x="32" y="25" font-family="Roboto,sans-serif" font-size="8" fill="#fff" stroke="none" text-anchor="middle">25</text><text x="32" y="32" font-family="Roboto,sans-serif" font-size="5" fill="#fff" stroke="none" text-anchor="middle">Jahre</text></svg>
        25 Jahre<br>Erfahrung
      </div>
      <div class="feature">
        <svg viewBox="0 0 64 64" fill="none" stroke="#fff" stroke-width="2"><circle cx="32" cy="26" r="21"/><circle cx="32" cy="26" r="12"/><path d="M32 19l2.2 4.6 5 .6-3.7 3.4 1 5-4.5-2.5-4.5 2.5 1-5-3.7-3.4 5-.6z"/><path d="M20 44l-6 14 8-3 4 7 6-12M44 44l6 14-8-3-4 7-6-12"/></svg>
        Hochwertige<br>Ausrüstung
      </div>
      <div class="feature">
        <svg viewBox="0 0 64 64" fill="none" stroke="#fff" stroke-width="2"><path d="M32 36l-11-11a6.5 6.5 0 0 1 11-7 6.5 6.5 0 0 1 11 7z"/><path d="M8 46l10-5h14l4 3H24M8 56h30l18-12-4-3-14 7"/><path d="M32 2v6M16 8l3 4M48 8l-3 4M6 22h5M53 22h5"/></svg>
        Umfassender<br>Service
      </div>
      <div class="feature">
        <svg viewBox="0 0 64 64" fill="none" stroke="#fff" stroke-width="2"><circle cx="32" cy="18" r="8"/><path d="M18 54V38c0-6 6-10 14-10s14 4 14 10v16"/><circle cx="12" cy="28" r="5"/><path d="M2 54V44c0-4 4-7 10-7"/><circle cx="52" cy="28" r="5"/><path d="M62 54V44c0-4-4-7-10-7"/></svg>
        engagiertes<br>Team
      </div>
    </div>
    <footer class="footer">
      <div class="footer__name">ALPENTON</div>
      <div class="footer__contact">Talweg 14 | 6430 Schwyz | 041 555 20 40<br>mail@alpen-ton.ch | www.alpen-ton.ch</div>
    </footer>
  </section>

  <section class="page page--back">
    <h1 class="services-title">UNSERE <span class="accent">LEISTUNGEN</span></h1>

    <div class="service-photo" style="left:32px;top:110px;background:linear-gradient(135deg,#8a6b4c,#c8b496 60%,#9c8e7c)" role="img" aria-label="Foto: schlanker Wandlautsprecher neben einem Blumenschmuck in der Kirche"></div>
    <div class="service" style="left:187px;top:106px;width:330px">
      <h2 class="accent">BESCHALLUNG</h2>
      <p>Die Anforderungen in akustisch schwierigen Räumen sind sehr hoch. Neuartige Beschallungskonzepte mit Beam-Steering Technologie machen eine hohe Sprachverständlichkeit in Kirchenräumen mit langer Nachhallzeit möglich. Zusammen mit einer normgerechten Installation einer Gehörlosenschlaufe können alle am Gottesdienst teilnehmen.</p>
    </div>

    <div class="service" style="left:32px;top:236px;width:320px">
      <h2><span class="accent">LED</span> BELEUCHTUNG</h2>
      <p>Eine neue stromsparende Beleuchtung ist für einen verantwortungsvollen Energieeinsatz unumgänglich. Die stromsparenden LED-Leuchten sind durch die sehr lange Lebensdauer wartungsfrei und sehr kosteneffizient. Moderne LED-Leuchtmittel sind zudem flickerfrei, dimmbar und in der richtigen Farbtemperatur erhältlich.</p>
    </div>
    <div class="service-photo" style="left:358px;top:241px;background:linear-gradient(180deg,#e0cfb4,#b48a5a 55%,#4a3526)" role="img" aria-label="Foto: beleuchteter Kirchenraum mit Gemeinde, von der Empore aus gesehen"></div>

    <div class="service-photo" style="left:32px;top:367px;background:linear-gradient(135deg,#3a3a38,#1e2120 50%,#5a4a3a)" role="img" aria-label="Foto: Steuerungsgeräte im Technikrack"></div>
    <div class="service" style="left:187px;top:370px;width:330px">
      <h2><span class="accent">INTERGRATION</span>/STEUERUNG</h2>
      <p>Beleuchtung, Beschallung, Projektion, Liedanzeige, Glockensteuerung und Friedhofsbeleuchtung. Viele Systeme zusammengeführt in eine übersichtliche und erweiterbare Steuerung über Netzwerk.</p>
    </div>

    <div class="service" style="left:32px;top:498px;width:320px">
      <h2><span class="accent">LIEDER</span>/TEXTANZEIGEN</h2>
      <p>Kostengünstige Liedanzeigen mit 8 Zeilen in allen Farbkombinationen. Auch Bilder können angezeigt werden (z.B. für Beerdigungen /Hochzeiten/Taufen usw).</p>
    </div>
    <div class="service-photo" style="left:358px;top:489px;background:linear-gradient(160deg,#5e6a4e,#7e9a5a 45%,#4a3a30)" role="img" aria-label="Foto: geöffnete Elektronik einer Liedanzeige mit Platinen und Kabeln"></div>

    <div class="cta">KONTAKTIEREN SIE UNS UNVERBINDLICH FÜR EIN<br>PERSÖNLICHES BERATUNGSGESPRÄCH.</div>

    <footer class="footer">
      <div class="footer__name">ALPENTON</div>
      <div class="footer__contact">Talweg 14 | 6430 Schwyz | 041 555 20 40<br>mail@alpen-ton.ch | www.alpen-ton.ch</div>
    </footer>
  </section>

</div>
</body>
</html>
```